Rusty Lantern Ale Room & Sports Kitchen Menu

This is my dine in menu for my sports bar. I would like it to be playful and fun. The colors of my logo are also the colors of my bar. You can look at facebook or rustylanternaleroom.com to see pictures. My current menu is a trifold and I would like to move away from that design. I like a the menu to flow, but am very open to new concepts. I feel like my current one is too boring and not professional enough as well as not catchy. I like a colored page, with colored lettering not necessarily black or white text. I currently use the colors of my log on my menu but like the idea of something that is not boring.

Target Market(s)

customers coming into my bar

Industry/Entity Type

Sports Bar

Requirements
Must have
• LOGO, Specials,
Nice to have
• pictures of food
Should not have
• open to all designs

```html
<!DOCTYPE html>
<html lang="en">
<head>
<meta charset="utf-8">
<title>Rusty Lantern Ale Room &amp; Sports Kitchen — Menu</title>
<link rel="stylesheet" href="https://fonts.googleapis.com/css2?family=Bebas+Neue&family=Montserrat:wght@500;600;700&family=Oleo+Script:wght@400;700&family=Zilla+Slab:wght@500;600;700&display=swap">
<style>
  :root{
    --slate:#5c5d5e;
    --slate-dark:#4d4e4f;
    --gold:#e9a329;
    --cream:#e8e4dc;
    --rule:#8a8b8c;
    --wing-1:#c9622a;
    --wing-2:#8e3a17;
    --plate:#d9d8d4;
  }
  *{box-sizing:border-box;margin:0;padding:0}
  html,body{width:1199px;height:1200px;overflow:hidden;background:#9aad9c}
  .menu{
    position:relative;width:1199px;height:1200px;overflow:hidden;
    background:radial-gradient(ellipse at 40% 35%, #666768 0%, var(--slate) 55%, var(--slate-dark) 100%);
    color:var(--cream);font-family:"Montserrat",sans-serif;
    display:grid;grid-template-columns:minmax(0,345px) minmax(0,1fr) minmax(0,345px);gap:0 36px;padding:48px 44px;
    align-items:start;
  }
  .col{position:relative;min-width:0;overflow-wrap:break-word}
  .section-title{font-family:"Bebas Neue",sans-serif;color:var(--gold);font-size:80px;letter-spacing:4px;line-height:.9}
  .script-title{font-family:"Oleo Script",cursive;color:var(--gold);font-size:56px;line-height:1}
  .rule{height:2px;background:var(--rule);margin:14px 0 20px}
  .item{margin-bottom:18px}
  .item-name{font-family:"Zilla Slab",serif;font-weight:700;color:var(--gold);font-size:23px;text-transform:uppercase;letter-spacing:.5px;line-height:1.05}
  .item-desc{font-size:12px;font-weight:600;text-transform:uppercase;letter-spacing:.5px;line-height:1.45;margin-top:4px}
  .price-list{font-family:"Zilla Slab",serif;font-weight:700;color:var(--gold);font-size:20px;text-transform:uppercase;line-height:1.45}
  .price-list span{color:var(--cream);font-family:"Montserrat",sans-serif;font-size:13px;font-weight:600}
  .philly{margin-top:30px}
  .philly .section-title{font-size:56px;letter-spacing:2px}
  .philly .sub{font-family:"Bebas Neue",sans-serif;color:var(--gold);font-size:28px;letter-spacing:13px}

  .wings-head{display:flex;align-items:center;gap:16px;margin-bottom:18px}
  .wing-photo{width:130px;height:130px;border-radius:50%;border:3px solid var(--gold);
    background:radial-gradient(circle at 45% 45%, var(--wing-1) 0%, var(--wing-2) 55%, var(--plate) 56%, #b8b7b3 100%);flex:none}
  .wings-title{font-family:"Oleo Script",cursive;color:var(--gold);font-size:52px;line-height:.95}
  .note{font-size:12px;font-weight:600;text-transform:uppercase;letter-spacing:.5px;line-height:1.6}
  .sauces{margin-top:16px;font-size:12px;font-weight:600;text-transform:uppercase;letter-spacing:.5px;line-height:1.6}
  .style-box{margin-top:30px;border:2px solid var(--gold);padding:24px 20px;text-align:center}
  .style-name{font-family:"Bebas Neue",sans-serif;color:var(--gold);font-size:72px;letter-spacing:4px;line-height:.9}
  .style-sub{font-family:"Bebas Neue",sans-serif;color:var(--gold);font-size:28px;letter-spacing:16px;margin-bottom:12px}
  .style-mark{display:inline-block;width:14px;height:14px;border-radius:50%;background:var(--gold);vertical-align:middle;margin-right:12px}

  .sand-intro{font-size:12.5px;font-weight:600;text-transform:uppercase;letter-spacing:.5px;line-height:1.5;margin:10px 0 20px}
  .footer{position:absolute;left:44px;right:44px;bottom:22px;display:flex;justify-content:space-between;
    font-family:"Zilla Slab",serif;font-weight:600;color:var(--gold);font-size:16px;letter-spacing:1px;text-transform:uppercase}
</style>
</head>
<body>
<main class="menu">
  <section class="col starters">
    <h2 class="section-title">Starters</h2>
    <div class="rule"></div>
    <div class="item"><div class="item-name">Sampler Platter</div><p class="item-desc">Provolone sticks, boneless wings, pierogies and chips with queso — 14.95</p></div>
    <div class="item"><div class="item-name">Jalapeño &amp; Cheddar Pierogies (6)</div><p class="item-desc">Potato and cheddar pockets with jalapeño, fried golden — 7.95</p></div>
    <div class="item"><div class="item-name">Provolone Cheese Sticks (6)</div><p class="item-desc">Served with marinara — 8.49</p></div>
    <div class="item"><div class="item-name">Potato Skins (6)</div><p class="item-desc">Loaded with cheddar and bacon, sour cream on the side — 7.95</p></div>
    <div class="price-list">
      Popcorn Shrimp w/ Fries <span>8.45</span><br>
      Chips &amp; Queso <span>6.49</span><br>
      Queso Refill <span>2.00</span><br>
      Chip Refill <span>1.00</span><br>
      Mini Corn Dogs (12) <span>6.49</span><br>
      Basket of Fries <span>2.99</span><br>
      Onion Rings <span>6.49</span>
    </div>
    <div class="philly">
      <h2 class="section-title">Original Philly</h2>
      <div class="sub">Cheesesteaks</div>
      <div class="rule"></div>
      <p class="item-desc">All steaks served on a toasted hoagie roll with fries</p>
      <div class="item" style="margin-top:12px"><div class="item-name">Classic Philly</div><p class="item-desc">Shaved ribeye, grilled onions and provolone — 10.95</p></div>
      <div class="item"><div class="item-name">Mushroom Philly</div><p class="item-desc">Steak, mushrooms, peppers and white American — 11.45</p></div>
    </div>
  </section>

  <section class="col wings">
    <div class="wings-head">
      <div class="wing-photo" role="img" aria-label="Photo of glazed jumbo chicken wings on a plate"></div>
      <h2 class="wings-title">Jumbo<br>Wings</h2>
    </div>
    <p class="note">Add a side of fries or chips with wings — 2.00<br>Finally, wings with some meat on them!<br>Wings are jointed wings, a flat and drumstick together.</p>
    <div class="rule"></div>
    <div class="item"><div class="item-name">Jumbo Traditional Wings</div><p class="item-desc">3 jointed wings (3 flats &amp; 3 drums) — 8.95<br>6 jointed wings (6 flats &amp; 6 drums) — 16.95</p></div>
    <div class="item"><div class="item-name">Boneless Wings</div><p class="item-desc">12 wings — 8.95 &nbsp;·&nbsp; 24 wings — 17.95</p></div>
    <div class="item"><div class="item-name">Chicken Tender (4) Basket</div><p class="item-desc">W/ fries or chips — 12.95</p></div>
    <p class="sauces">Sauce choices: Bourbon BBQ, Medium, Thai Zing, Mango Habanero, Hot (with jalapeño), Scorchin' (with habanero peppers), Lantern Punch (with ghost peppers)</p>
    <div class="style-box">
      <div class="style-name"><span class="style-mark"></span>Lantern</div>
      <div class="style-sub">Style</div>
      <p class="note">(The fries come on the sub!) These subs come stacked: meat is thrown on the roll with fries piled right on top.</p>
    </div>
  </section>

  <section class="col sandwiches">
    <h2 class="script-title">Sandwiches</h2>
    <p class="sand-intro">All sandwiches come on a roll with fries or chips</p>
    <div class="item"><div class="item-name">Italian Sausage</div><p class="item-desc">½ pound of sausage covered with onions &amp; peppers on a hoagie roll. You can't resist! — 10.95</p></div>
    <div class="item"><div class="item-name">Bacon &amp; Jalapeño Grilled Cheese</div><p class="item-desc">Half pound of bacon (6 slices) — 10.95</p></div>
    <div class="item"><div class="item-name">Buffalo Ranch Chicken Sandwich</div><p class="item-desc">Ranch and medium sauce on a breaded chicken breast — 10.95</p></div>
    <div class="item"><div class="item-name">Grilled Chicken</div><p class="item-desc">(8 oz) Seasoned breast with lettuce and tomato — 10.95</p></div>
    <div class="item"><div class="item-name">Gyro</div><p class="item-desc">Gyro meat, onions and tomato on pita, the meat sliced fresh with tzatziki — 10.95</p></div>
  </section>

  <footer class="footer">
    <span>Rusty Lantern Ale Room &amp; Sports Kitchen</span>
    <span>rustylanternaleroom.com</span>
  </footer>
</main>
</body>
</html>
```